Instagram ad design required

For an IT system house, we need an ad design for a job recruiting campaign on Instagram. A great engaging advertisement is required that encourages potential applicants to click on the ad. The recruiting funnel already exists, only an Instagram ad image should be designed. Follow-up orders for further campaigns as well as Facebook and LinkedIn are possible.
The design of the IT system house Dolvira serves as a design inspiration: www.dolvira.com
The customer should be perceived as a great, modern employer. The target group are young IT technicians who want to work in a cool and modern company. For example, the topic could be IT Super Hero wanted with corresponding graphic content.
Target Market(s)
IT system technician
Industry/Entity Type
Informatik
Other font styles liked:
- PT Sans
Look and feel

```html
<!DOCTYPE html>
<html lang="en">
<head>
<meta charset="utf-8">
<title>Dolvira – We Are Hiring</title>
<link rel="stylesheet" href="https://fonts.googleapis.com/css2?family=Montserrat:wght@400;500;600;700;800&display=swap">
<style>
  :root{
    --frame-green:#80c342;
    --deep-green:#00874a;
    --cream:#f2f6e8;
    --lime:#c8de6f;
    --ink:#1c1c1c;
    --white:#ffffff;
  }
  *{margin:0;padding:0;box-sizing:border-box}
  html,body{width:1200px;height:1200px;overflow:hidden;background:var(--frame-green)}
  body{font-family:"Montserrat",sans-serif;position:relative}
  .ad{position:absolute;inset:0;background:var(--frame-green)}
  .panel{position:absolute;left:65px;top:65px;width:1070px;height:973px;background:var(--cream)}
  .brand-tab{position:absolute;left:500px;top:0;width:237px;height:66px;background:var(--cream)}
  .brand-name{position:absolute;left:500px;top:110px;width:237px;text-align:center;
    font-weight:800;font-size:36px;letter-spacing:1px;color:var(--deep-green)}
  .hero-band{position:absolute;left:65px;top:215px;width:1070px;height:571px;background:var(--deep-green)}
  .portrait{position:absolute;left:610px;top:150px;width:525px;height:636px;
    border-radius:230px 230px 0 0;
    background:linear-gradient(180deg,#3b3f45 0%,#23262b 55%,#15171a 100%)}
  .headline{position:absolute;left:122px;color:var(--lime);line-height:1}
  .we-are{top:318px;font-size:60px;font-weight:600}
  .hiring{top:378px;font-size:108px;font-weight:800;letter-spacing:-2px}
  .divider{position:absolute;left:122px;top:503px;width:470px;border-top:3px dotted var(--lime)}
  .we-want{top:522px;font-size:58px;font-weight:600}
  .super-hero{top:580px;font-size:90px;font-weight:800;line-height:0.92;
    color:transparent;-webkit-text-stroke:3px var(--lime);letter-spacing:-2px}
  .position-label{position:absolute;left:118px;top:838px;font-size:30px;font-weight:700;color:var(--ink)}
  .position-rule{position:absolute;left:118px;top:889px;width:968px;border-top:2px dotted #9a9a9a}
  .arrow-box{position:absolute;left:118px;top:903px;width:82px;height:78px;background:var(--frame-green)}
  .arrow-box svg{width:100%;height:100%}
  .job-title{position:absolute;left:224px;top:908px;font-size:62px;font-weight:800;color:var(--ink);letter-spacing:-1px}
  .apply-btn{position:absolute;left:834px;top:903px;width:252px;height:78px;border-radius:8px;
    background:var(--frame-green);color:var(--cream);font-size:32px;font-weight:700;
    display:flex;align-items:center;justify-content:center}
  .contact{position:absolute;top:1078px;display:flex;align-items:center;gap:20px;color:var(--white)}
  .contact-email{left:65px}
  .contact-web{left:607px}
  .contact-icon{width:70px;height:70px;background:var(--cream);flex:none}
  .contact-icon svg{width:100%;height:100%}
  .contact-label{font-size:20px;font-weight:500;line-height:1.1}
  .contact-value{font-size:27px;font-weight:600;line-height:1.2}
  .contact-web .contact-value{font-size:25px}
</style>
</head>
<body>
<div class="ad">
  <div class="panel"></div>
  <div class="brand-tab"></div>
  <div class="hero-band"></div>
  <div class="portrait" role="img" aria-label="Photo of a young professional in a dark suit and glasses holding a tablet"></div>
  <div class="brand-name">DOLVIRA</div>

  <div class="headline we-are">WE ARE</div>
  <div class="headline hiring">HIRING !</div>
  <div class="divider"></div>
  <div class="headline we-want">WE WANT</div>
  <div class="headline super-hero">IT SUPER<br>HERO</div>

  <div class="position-label">POSITION :</div>
  <div class="position-rule"></div>
  <div class="arrow-box">
    <svg viewBox="0 0 82 78"><polyline points="30,20 52,39 30,58" fill="none" stroke="#f2f6e8" stroke-width="11" stroke-linejoin="miter"/></svg>
  </div>
  <div class="job-title">IT TECHNICIAN</div>
  <div class="apply-btn">APPLY NOW</div>

  <div class="contact contact-email">
    <div class="contact-icon">
      <svg viewBox="0 0 70 70"><rect x="14" y="20" width="42" height="30" fill="none" stroke="#80c342" stroke-width="3"/><polyline points="14,20 35,38 56,20" fill="none" stroke="#80c342" stroke-width="3"/></svg>
    </div>
    <div>
      <div class="contact-label">EMAIL YOUR RESUME :</div>
      <div class="contact-value">recruiting@dolvira.com</div>
    </div>
  </div>

  <div class="contact contact-web">
    <div class="contact-icon">
      <svg viewBox="0 0 70 70" fill="none" stroke="#80c342" stroke-width="3"><circle cx="35" cy="35" r="20"/><ellipse cx="35" cy="35" rx="9" ry="20"/><line x1="15" y1="35" x2="55" y2="35"/><line x1="18" y1="25" x2="52" y2="25"/><line x1="18" y1="45" x2="52" y2="45"/></svg>
    </div>
    <div>
      <div class="contact-label">MORE INFORMATION :</div>
      <div class="contact-value">https://www.dolvira.com/de-en</div>
    </div>
  </div>
</div>
</body>
</html>
```